New Townhome community needs for sale sign.

need a 4 foot by 8 foot banner to put on building listing newly constructed townhomes as "coming soon" to market. Construction is scheduled to be completed Dec 2024. Sale of units will begin Spring of 2025.
6 individual townhome units each 2,000 square feet. each unit is 3 bedroom 2.5 bathroom with 2 car garage and each has a rooftop "sky lounge" with amazing views. Gated community. Units available for sale Spring of 2025. Real estate company selling units will be KTL & Associates. Will need KTL & Associates Logo on the banner. Would like to keep with the same blue color scheme as the KTL & Associates logo. phone number on banner to be 480-555-3164. web ktlpartners.example.

```html
<!DOCTYPE html>
<html lang="en">
<head>
<meta charset="utf-8">
<title>KTL &amp; Associates – Coming Soon Banner</title>
<link rel="stylesheet" href="https://fonts.googleapis.com/css2?family=Source+Sans+3:wght@300;700;900&family=Roboto:wght@400;700&display=swap">
<style>
  :root {
    --sky: #27a6d7;
    --ocean: #1d6fa3;
    --ink: #2b2b2b;
    --shade: #d6d9de;
    --paper: #ffffff;
    --backdrop: #e8ebee;
  }
  * { margin: 0; padding: 0; box-sizing: border-box; }
  html, body { width: 1200px; height: 1200px; overflow: hidden; background: var(--backdrop); }
  .banner {
    position: absolute; left: 300px; top: 0;
    width: 600px; height: 1200px;
    background: var(--paper);
    overflow: hidden;
    font-family: "Source Sans 3", sans-serif;
  }
  .brand {
    position: absolute; top: 86px; left: 0; width: 100%;
    display: flex; justify-content: center; align-items: center; gap: 12px;
  }
  .brand-mark { width: 34px; height: 34px; background: var(--ocean); }
  .brand-name {
    font-family: "Source Sans 3", sans-serif; font-weight: 700;
    font-size: 42px; line-height: 48px; color: var(--ink); letter-spacing: -0.5px;
  }
  .announce-graphic {
    position: absolute; left: 146px; top: 172px; width: 310px; height: 236px;
    background: linear-gradient(160deg, var(--sky) 0%, var(--sky) 45%, var(--ocean) 80%, var(--shade) 100%);
  }
  .headline {
    position: absolute; top: 448px; left: 0; width: 100%;
    text-align: center; font-size: 50px; line-height: 55px;
    color: var(--ink); font-weight: 300; letter-spacing: -0.3px;
  }
  .headline .light-blue { color: var(--sky); font-weight: 900; }
  .headline .dark-blue { color: var(--ocean); font-weight: 900; }
  .unit-count {
    position: absolute; left: 53px; top: 605px; width: 502px; height: 62px;
    border-radius: 31px; background: var(--ocean); color: var(--paper);
    font-family: "Roboto", sans-serif; font-weight: 700; font-size: 33px;
    letter-spacing: 1px; display: flex; align-items: center; justify-content: center;
  }
  .features { position: absolute; left: 153px; top: 695px; width: 294px; list-style: none; }
  .features li {
    height: 43px; margin-bottom: 6px; border-radius: 22px;
    background: var(--ocean); color: var(--paper);
    font-family: "Roboto", sans-serif; font-size: 26px;
    display: flex; align-items: center; justify-content: center;
  }
  .rooftop {
    position: absolute; top: 905px; left: 0; width: 100%; text-align: center;
    font-family: "Roboto", sans-serif; font-weight: 700; font-size: 27px;
    line-height: 34px; color: var(--sky);
  }
  .rooftop .lounge { color: var(--ocean); }
  .contact-band {
    position: absolute; left: 0; top: 1036px; width: 100%; height: 164px;
    background: var(--sky);
  }
  .web-pill {
    position: absolute; left: 110px; top: 1003px; width: 380px; height: 68px;
    border: 4px solid var(--paper); border-radius: 34px; background: var(--sky);
    display: flex; align-items: center; justify-content: center;
    font-family: "Roboto", sans-serif; font-weight: 700; font-size: 34px;
    color: var(--paper);
  }
  .web-pill .dark { color: var(--ink); }
  .phone {
    position: absolute; top: 1080px; left: 0; width: 100%; text-align: center;
    font-family: "Roboto", sans-serif; font-weight: 700; font-size: 88px;
    color: var(--paper); letter-spacing: 1px; line-height: 100px;
  }
  .phone .dot { color: var(--ocean); }
</style>
</head>
<body>
<main class="banner">
  <header class="brand">
    <span class="brand-mark"></span>
    <span class="brand-name">KTL &amp; Associates</span>
  </header>

  <div class="announce-graphic" role="img" aria-label="Coming soon ribbon graphic with megaphone"></div>

  <h1 class="headline">
    <span class="light-blue">UNITS AVAILABLE</span> FOR<br>
    SALE <span class="dark-blue">SPRING OF 2025</span>
  </h1>

  <div class="unit-count">6 INDIVIDUAL TOWNHOME</div>

  <ul class="features">
    <li>2,000 Square Feet</li>
    <li>3 Bedroom</li>
    <li>2.5 Bathroom</li>
    <li>2 Car Garage</li>
  </ul>

  <p class="rooftop">Each Has A Rooftop<br><span class="lounge">"Sky Lounge"</span> With Amazing Views</p>

  <div class="contact-band"></div>
  <div class="web-pill">ktl<span class="dark">partners</span>.example</div>
  <div class="phone">480<span class="dot">.</span>555<span class="dot">.</span>3164</div>
</main>
</body>
</html>
```